Northern Terrain Published Photographer Website

I need a website to feature a home page slide show of 6 of my top photos then a few simple pages including; gallery, bio, social, checkout, services
Updates

Need extra days to review

Target Market(s)

photography

Industry/Entity Type

Photographer

Coding

Coded - Design and coding required

Number of Pages Required

5+ page

Colors

Designer to choose colors to be used in the design.

Requirements
Must have
• clean eye catching elegant trendy
Nice to have
• unique and creative from other photographer websites

```html
<!DOCTYPE html>
<html lang="en">
<head>
<meta charset="utf-8">
<title>Northern Terrain — Photography</title>
<link rel="stylesheet" href="https://fonts.googleapis.com/css2?family=Lato:ital,wght@0,400;0,700;0,900;1,400&family=Montserrat:wght@400;500&display=swap">
<style>
:root{
  --orange:#f7941d;
  --blue:#1f8fd6;
  --ink:#1b1b1b;
  --grey:#8a8a8a;
  --white:#ffffff;
  --night:#121212;
  --green:#7cc242;
}
*{margin:0;padding:0;box-sizing:border-box}
html,body{width:1200px;height:2478px;overflow:hidden;background:var(--white)}
body{position:relative;font-family:'Lato',sans-serif;color:var(--ink)}
.abs{position:absolute}

/* hero */
.hero{left:0;top:0;width:1200px;height:750px;
  background:linear-gradient(180deg,#2c3d5c 0%,#4a5563 50%,#2a3020 100%)}
.brand-badge{left:115px;top:-87px;width:222px;height:222px;border-radius:50%;background:var(--white);
  display:flex;align-items:flex-end;justify-content:center;padding-bottom:46px}
.brand-badge span{font-style:italic;font-size:30px;line-height:45px;text-align:center;color:var(--ink)}
.nav{top:42px;left:375px;width:762px;display:flex;justify-content:space-between}
.nav a{color:var(--white);font-weight:700;font-size:17px;text-decoration:none;text-transform:uppercase}
.hero-title{top:265px;left:0;width:1200px;text-align:center;color:var(--white);font-weight:900;font-size:70px;letter-spacing:-1px}
.hero-tag{top:372px;left:0;width:1242px;text-align:center;color:var(--white);font-size:27px;font-weight:700}
.btn-solid{left:502px;top:454px;width:195px;height:56px;background:var(--orange);color:var(--white);
  font-size:20px;letter-spacing:2px;font-weight:700;display:flex;align-items:center;justify-content:center}
.dots{top:671px;left:539px;display:flex;gap:8px}
.dots i{width:13px;height:13px;border-radius:50%;background:var(--white);display:block}
.dots i.on{background:var(--orange)}
.camera-tab{left:527px;top:706px}

/* about */
.cross{background:var(--blue)}
.about-photo{left:125px;top:920px;width:351px;height:238px;
  background:linear-gradient(180deg,#5d8fbf 0%,#8c8a86 100%)}
.about-title{left:599px;top:880px;font-size:35px;font-weight:900;letter-spacing:-.5px}
.about-title em{font-style:normal;color:var(--orange)}
.about-lead{left:601px;top:946px;width:400px;font-size:16px;line-height:26px;font-weight:700;color:var(--ink)}
.about-body{left:601px;top:1002px;width:420px;font-size:16px;line-height:26px;color:var(--grey)}
.btn-line{left:604px;top:1133px;width:150px;height:43px;border:2px solid var(--orange);color:var(--orange);
  font-size:17px;font-weight:700;display:flex;align-items:center;justify-content:center}

/* gallery */
.gallery{left:0;top:1289px;width:1200px;height:680px;
  background:linear-gradient(180deg,#e2e8ed 0%,#ebe6df 100%)}
.gallery-title{left:0;top:1350px;width:1190px;text-align:center;font-size:43px;font-weight:700;color:#2a2a2a}
.shot{position:absolute}
.arrow{position:absolute}

/* footer */
.footer{left:0;top:1960px;width:1200px;height:464px;background:var(--night)}
.foot-brand{left:100px;top:2108px;width:240px;text-align:center;color:var(--white);font-size:43px;font-weight:700;line-height:52px}
.foot-about{left:122px;top:2244px;width:218px;text-align:center;color:var(--white);font-size:16px;font-weight:700;line-height:23px}
.foot-head{color:var(--white);font-family:'Montserrat',sans-serif;font-size:12px;font-weight:500;text-transform:uppercase}
.foot-head::after{content:"";display:block;width:32px;height:1px;background:var(--white);margin-top:11px}
.foot-text{color:#d8d8d8;font-family:'Montserrat',sans-serif;font-size:14px;line-height:21px}
.links{left:671px;top:2152px;list-style:none}
.links li{color:#d8d8d8;font-family:'Montserrat',sans-serif;font-size:14px;line-height:18px;margin-bottom:16px}
.news-field{left:822px;top:2170px;width:202px;height:43px;background:var(--white);font-family:'Montserrat',sans-serif;
  font-size:12px;color:#9a9a9a;padding:14px 0 0 9px}
.news-join{left:1023px;top:2170px;width:60px;height:43px;background:var(--orange);font-family:'Montserrat',sans-serif;
  font-size:11px;font-weight:500;color:var(--ink);display:flex;align-items:center;justify-content:center}
.social{left:822px;top:2243px;display:flex;gap:22px}
.social span{color:var(--white);font-family:'Montserrat',sans-serif;font-size:12px;font-weight:500;
  border:1px solid #6a6a6a;padding:3px 7px}
.legal{left:0;top:2424px;width:1200px;height:54px;background:#0a0a0a;color:var(--white);font-size:13px;padding:19px 0 0 111px}
</style>
</head>
<body>

<div class="abs hero" role="img" aria-label="Landscape photograph of mountains at sunset"></div>
<div class="abs brand-badge"><span>NORTHERN<br>TERRAIN</span></div>
<nav class="abs nav">
  <a>Home</a><a>Gallery</a><a>Bio</a><a>Social</a><a>Checkout</a><a>Services</a><a>About Us</a><a>Contact</a>
</nav>
<h1 class="abs hero-title">NORTHERN TERRAIN</h1>
<p class="abs hero-tag">Photography is an austere and blazing poetry of the real</p>
<div class="abs btn-solid">READ MORE</div>
<div class="abs dots"><i></i><i></i><i class="on"></i><i></i><i></i><i></i></div>
<svg class="abs camera-tab" width="132" height="46" viewBox="0 0 132 46">
  <path d="M0 46 C28 46 26 0 66 0 C106 0 104 46 132 46 Z" fill="#ffffff"/>
  <rect x="40" y="16" width="62" height="42" rx="8" fill="#1f8fd6"/>
  <rect x="56" y="11" width="22" height="10" rx="3" fill="#1f8fd6"/>
  <circle cx="66" cy="37" r="13" fill="#ffffff"/>
  <circle cx="66" cy="37" r="8" fill="#1f8fd6"/>
  <circle cx="92" cy="25" r="3" fill="#ffffff"/>
</svg>

<div class="abs cross" style="left:294px;top:822px;width:2px;height:80px"></div>
<div class="abs cross" style="left:294px;top:1176px;width:2px;height:80px"></div>
<div class="abs cross" style="left:23px;top:1040px;width:80px;height:2px"></div>
<div class="abs cross" style="left:491px;top:1040px;width:80px;height:2px"></div>
<div class="abs about-photo" role="img" aria-label="Photograph of the photographer walking a dog on a seaside pier"></div>
<h2 class="abs about-title">ABOUT <em>US</em></h2>
<p class="abs about-lead">Lorem ipsum dolor sit amet, consectetur adipiscing elit, sed do eiusmod</p>
<p class="abs about-body">Sed ut perspiciatis unde omnis iste natus error sit voluptatem accusantium doloremque laudantium, totam rem aperiam, eaque ipsa quae ab illo inventore veritatis et quasi architecto beatae vitae dicta</p>
<div class="abs btn-line">READ MORE</div>

<section class="abs gallery" role="img" aria-label="Soft sky backdrop"></section>
<h2 class="abs gallery-title">Gallery</h2>
<div class="shot" style="left:109px;top:1471px;width:337px;height:426px;background:linear-gradient(180deg,#f0a424,#c9581c)" role="img" aria-label="Photograph of a golden sunset over a pier"></div>
<div class="shot" style="left:456px;top:1472px;width:330px;height:207px;background:linear-gradient(180deg,#4a5f82,#b9742c)" role="img" aria-label="Photograph of a pier at dusk"></div>
<div class="shot" style="left:456px;top:1690px;width:330px;height:208px;background:linear-gradient(180deg,#c82445,#9a1530)" role="img" aria-label="Photograph of a crimson sunset over a pier"></div>
<div class="shot" style="left:796px;top:1472px;width:290px;height:426px;background:linear-gradient(180deg,#7e9a48,#94ad5a)" role="img" aria-label="Photograph of an elk in a meadow"></div>
<svg class="arrow" style="left:34px;top:1662px" width="52" height="52" viewBox="0 0 52 52">
  <circle cx="26" cy="26" r="24.5" fill="none" stroke="#7cc242" stroke-width="2"/>
  <path d="M36 26H16M24 18l-8 8 8 8" fill="none" stroke="#7cc242" stroke-width="3" stroke-linecap="round" stroke-linejoin="round"/>
</svg>
<svg class="arrow" style="left:1108px;top:1662px" width="52" height="52" viewBox="0 0 52 52">
  <circle cx="26" cy="26" r="24.5" fill="none" stroke="#7cc242" stroke-width="2"/>
  <path d="M16 26h20M28 18l8 8-8 8" fill="none" stroke="#7cc242" stroke-width="3" stroke-linecap="round" stroke-linejoin="round"/>
</svg>

<footer class="abs footer"></footer>
<svg class="abs" style="left:0;top:1950px" width="1200" height="12" viewBox="0 0 1200 12">
  <path d="M0 8 L60 5 L120 7 L200 3 L280 6 L360 4 L440 7 L520 2 L600 6 L680 4 L760 7 L840 3 L920 6 L1000 4 L1080 7 L1140 3 L1200 6 L1200 12 L0 12 Z" fill="#121212"/>
</svg>
<div class="abs foot-brand">Northern<br>Terrain</div>
<p class="abs foot-about">Lorem ipsum dolor sit amet, consectetur adipiscing elit, sed do eiusmod</p>

<div class="abs foot-head" style="left:366px;top:2110px">Contact me</div>
<svg class="abs" style="left:361px;top:2158px" width="22" height="16" viewBox="0 0 22 16"><rect x="1" y="1" width="20" height="14" fill="none" stroke="#fff" stroke-width="2"/><path d="M1 1l10 8 10-8" fill="none" stroke="#fff" stroke-width="2"/></svg>
<p class="abs foot-text" style="left:397px;top:2155px">info@northernterrain.example</p>
<svg class="abs" style="left:365px;top:2210px" width="18" height="18" viewBox="0 0 18 18"><path d="M4 1l3 4-2 2c1 3 3 5 6 6l2-2 4 3-2 3C8 17 1 10 1 3z" fill="#fff"/></svg>
<p class="abs foot-text" style="left:393px;top:2208px">(02) 5550 1873<br>(02) 5550 1873</p>
<svg class="abs" style="left:367px;top:2280px" width="14" height="20" viewBox="0 0 14 20"><path d="M7 0a7 7 0 0 1 7 7c0 5-7 13-7 13S0 12 0 7a7 7 0 0 1 7-7z" fill="#fff"/><circle cx="7" cy="7" r="2.6" fill="#121212"/></svg>
<p class="abs foot-text" style="left:393px;top:2279px">48 Alder Row, dolor sit amet,<br>Consectetur adiping,</p>

<div class="abs foot-head" style="left:669px;top:2110px">Quick link</div>
<ul class="abs links">
  <li>Home</li><li>About us</li><li>Testimonials</li><li>Privacy Policy</li>
  <li>Terms &amp;<br>Conditions of Use</li><li>Conduct Code &amp;<br>Code of Ethics</li>
</ul>

<div class="abs foot-head" style="left:820px;top:2110px">Newsletter</div>
<div class="abs news-field">Email</div>
<div class="abs news-join">JOIN</div>
<div class="abs social"><span>Share</span><span>Follow</span><span>Connect</span></div>

<div class="abs legal">© 2019 All Rights Reserved | Privacy Policy | Terms and Conditions</div>

</body>
</html>
```